PowerPoint Design Project

We need a powerpoint design for our consulting company, Halvern Consulting. We provide technology strategy and solutioning services, with an emphasis on cloud technology. More information about our services can be found at www.halvernconsulting-example.com

We are looking for a design that is professional, but not corporate stuffy. The design needs to use our primary colors in our brand.
Updates

Reason: We need to iterate on some of the great designs, plus, many people have not had a chance to submit their design yet.

Reason: We had a lot of people accept the project, but not all of them have responded yet. We wanted to get them some time, plus, ask a couple of people to make some minor revisions.

Target Market(s)

Technology buyers between the ages of 30-55 at Pinnacle 900 companies

Industry/Entity Type

It Company

Requirements
Must have
• Must follow our logo colors.
Must have at least a cover slide and interior content slide.
Should not have
• Should not contain anything cartoonish or anything with lots of clouds

```html
<!DOCTYPE html>
<html lang="en">
<head>
<meta charset="utf-8">
<title>Commonalities between 3 products – Halvern Consulting</title>
<link href="https://fonts.googleapis.com/css2?family=Open+Sans:ital,wght@0,400;0,600;0,700;1,800&display=swap" rel="stylesheet">
<style>
  :root {
    --bg: #cdcfd1;
    --panel: #d9dbdc;
    --white: #ffffff;
    --blue: #2a7aa0;
    --blue-dark: #1f6688;
    --brown: #5e524a;
    --ink: #4a4a4a;
    --ink-soft: #5a5a5a;
    --grey-circle: #b6b6b6;
  }
  * { margin: 0; padding: 0; box-sizing: border-box; }
  html, body { width: 1200px; height: 900px; overflow: hidden; }
  body {
    background: var(--bg);
    font-family: "Open Sans", Arial, sans-serif;
    color: var(--ink);
    position: relative;
  }
  .slide-number {
    position: absolute; left: 23px; top: 53px; width: 37px; height: 37px;
    background: var(--blue); color: var(--white);
    font-style: italic; font-size: 22px; line-height: 37px; text-align: center;
  }
  .slide-title {
    position: absolute; left: 73px; top: 46px;
    font-size: 36px; font-weight: 800; font-style: italic; color: #555;
    letter-spacing: 0.3px;
  }
  .slide-title .accent { color: var(--blue); }
  .content-frame {
    position: absolute; left: 60px; top: 115px; width: 1078px; height: 600px;
    border: 10px solid var(--white); border-bottom: none;
    background: var(--panel);
  }
  .nav-arrow {
    position: absolute; top: 412px; width: 37px; height: 35px;
    background: var(--white);
  }
  .nav-arrow.prev { left: 73px; }
  .nav-arrow.next { left: 1087px; }
  .diagram { position: absolute; left: 0; top: 0; width: 1200px; height: 900px; }
  .example-list {
    position: absolute; list-style: none;
    font-size: 17px; line-height: 23px; color: var(--ink-soft);
  }
  .example-list li span { display: inline-block; width: 45px; }
  .list-top { left: 825px; top: 297px; }
  .list-left { left: 143px; top: 514px; }
  .list-right { left: 900px; top: 514px; }
  .band { position: absolute; top: 713px; height: 14px; }
  .band.brown { left: 57px; width: 246px; background: var(--brown); }
  .band.blue { left: 303px; width: 835px; background: var(--blue); }
  .footer {
    position: absolute; left: 60px; top: 727px; width: 1078px; height: 130px;
    background: var(--white);
  }
  .brand {
    position: absolute; left: 35px; top: 34px;
    display: flex; align-items: center; gap: 14px;
  }
  .brand-dot { width: 26px; height: 26px; border-radius: 50%; background: var(--blue); }
  .brand-name { font-size: 38px; font-weight: 400; color: var(--brown); letter-spacing: -0.5px; }
  .contact {
    position: absolute; right: 30px; top: 8px; text-align: right;
    font-size: 17px; line-height: 24px; color: var(--ink);
  }
  .contact-heading { font-size: 23px; font-weight: 700; color: var(--blue-dark); line-height: 30px; }
  .contact strong { color: var(--blue-dark); font-weight: 700; }
</style>
</head>
<body>
  <div class="slide-number">5</div>
  <h1 class="slide-title">Commonalities <span class="accent">between 3 products</span></h1>

  <div class="content-frame"></div>

  <div class="nav-arrow prev"></div>
  <div class="nav-arrow next"></div>

  <svg class="diagram" viewBox="0 0 720 540" aria-label="Venn diagram of three products">
    <!-- navigation triangles -->
    <polygon points="62,249 62,266 48,257.5" fill="#8a8a8a"/>
    <polygon points="656,249 656,266 670,257.5" fill="#8a8a8a"/>

    <!-- circles -->
    <circle cx="362" cy="176" r="71" fill="var(--grey-circle)" opacity="0.9"/>
    <circle cx="307" cy="280" r="71" fill="#6d625a" opacity="0.85"/>
    <circle cx="412" cy="280" r="71" fill="#2f7fa5" opacity="0.85"/>

    <g font-family="Open Sans, Arial, sans-serif" font-size="11" fill="#4a4a4a" text-anchor="middle">
      <text x="362" y="181">PRODUCT 1</text>
      <text x="291" y="284">PRODUCT 3</text>
      <text x="428" y="284">PRODUCT 2</text>
    </g>
    <g font-family="Open Sans, Arial, sans-serif" font-size="6.5" fill="#ffffff" text-anchor="middle">
      <text transform="translate(324,229) rotate(35)">LOREM</text>
      <text transform="translate(393,232) rotate(-35)">LOREM</text>
      <text transform="translate(362,287) rotate(90)">LOREM</text>
    </g>

    <!-- connectors -->
    <g stroke="#6a6a6a" stroke-width="0.8">
      <line x1="415" y1="160" x2="488" y2="160"/>
      <line x1="167" y1="293" x2="247" y2="293"/>
      <line x1="473" y1="293" x2="533" y2="293"/>
    </g>
    <g fill="#ffffff" stroke="#8a8a8a" stroke-width="0.5">
      <circle cx="415" cy="160" r="2.6"/>
      <circle cx="247" cy="293" r="2.6"/>
      <circle cx="473" cy="293" r="2.6"/>
    </g>

    <!-- example tags -->
    <g fill="var(--blue)">
      <rect x="488" y="152" width="88" height="19"/>
      <rect x="79" y="284" width="88" height="19"/>
      <rect x="533" y="284" width="87" height="19"/>
    </g>
    <g font-family="Open Sans, Arial, sans-serif" font-size="9" fill="#ffffff" text-anchor="middle">
      <text x="532" y="165">EXAMPLE</text>
      <text x="123" y="297">EXAMPLE</text>
      <text x="576.5" y="297">EXAMPLE</text>
    </g>
  </svg>

  <ol class="example-list list-top">
    <li><span>1.</span>Lorem</li>
    <li><span>2.</span>Dolor</li>
    <li><span>3.</span>Sit Amet</li>
  </ol>
  <ol class="example-list list-left">
    <li><span>1.</span>Lorem</li>
    <li><span>2.</span>Dolor</li>
    <li><span>3.</span>Sit Amet</li>
  </ol>
  <ol class="example-list list-right">
    <li><span>1.</span>Lorem</li>
    <li><span>2.</span>Dolor</li>
    <li><span>3.</span>Sit Amet</li>
  </ol>

  <div class="band brown"></div>
  <div class="band blue"></div>

  <footer class="footer">
    <div class="brand">
      <div class="brand-dot"></div>
      <div class="brand-name">Halvern Consulting</div>
    </div>
    <div class="contact">
      <div class="contact-heading">CONTACT US</div>
      <div>Your Address Here, State, Country</div>
      <div><strong>Phone:</strong> +123 456 7890</div>
      <div><strong>Email:</strong> enquiries@halvernconsulting-example.com</div>
    </div>
  </footer>
</body>
</html>
```